Brightwire Hollow Business cards

one side I would like my logo (uploaded) and the other side I want my details. I'm an electrician in sydney. The logo side I'm happy with just a white background and our logo in the middle.

Details for other side
24/7 Sydney Electrician
Marcus Pell
0431 587 219
marcus@brightwirehollow.com.au
brightwirehollow.com.au
icons for facebook, instagram, linked in

Industry/Entity Type

electrician

Contact Information for Business Card

company info

```html
<!DOCTYPE html>
<html lang="en">
<head>
<meta charset="utf-8">
<title>Brightwire Hollow – Business Cards</title>
<link href="https://fonts.googleapis.com/css2?family=Montserrat:wght@400;500;600;700;800&display=swap" rel="stylesheet">
<style>
  :root {
    --stage: #1b1b1c;
    --card-black: #141414;
    --card-white: #f7f7f6;
    --ink: #262626;
    --ink-soft: #3a3a3a;
    --red: #e0261f;
    --logo-grey: #8d8d8d;
    --edge-dark: #232323;
    --social-mid: #2d6db5;
    --social-dark: #1f4f8f;
  }
  * { box-sizing: border-box; margin: 0; padding: 0; }
  html, body {
    width: 1200px;
    height: 852px;
    overflow: hidden;
    background: var(--stage);
    font-family: "Montserrat", Arial, sans-serif;
  }
  .sheet {
    position: relative;
    width: 1200px;
    height: 852px;
    display: flex;
    align-items: center;
    justify-content: center;
    gap: 60px;
  }
  .card {
    position: relative;
    width: 500px;
    height: 290px;
    border-radius: 22px;
    overflow: hidden;
  }

  /* Logo side */
  .card--logo {
    background: var(--card-black);
    display: flex;
    align-items: center;
    justify-content: center;
  }
  .brand {
    display: flex;
    align-items: center;
    gap: 12px;
  }
  .brand__dot {
    width: 30px;
    height: 30px;
    border-radius: 50%;
    background: var(--red);
    flex: none;
  }
  .brand__name {
    font-weight: 800;
    text-transform: uppercase;
    letter-spacing: 0.02em;
    line-height: 1.05;
  }
  .card--logo .brand__name {
    font-size: 34px;
    color: var(--logo-grey);
  }

  /* Details side */
  .card--details {
    background: var(--card-white);
    border-bottom: 10px solid var(--edge-dark);
  }
  .card--details .brand {
    position: absolute;
    left: 30px;
    top: 118px;
    width: 200px;
    gap: 10px;
  }
  .card--details .brand__dot { width: 20px; height: 20px; }
  .card--details .brand__name {
    font-size: 22px;
    color: var(--ink);
  }
  .contact {
    position: absolute;
    left: 258px;
    top: 42px;
    width: 228px;
    color: var(--ink-soft);
  }
  .contact__name {
    font-size: 20px;
    font-weight: 700;
    color: var(--red);
    line-height: 1.1;
  }
  .contact__role {
    font-size: 11px;
    font-weight: 500;
    margin: 3px 0 10px 12px;
  }
  .contact__list { list-style: none; }
  .contact__item {
    display: flex;
    align-items: center;
    gap: 6px;
    font-size: 10.5px;
    font-weight: 500;
    line-height: 1;
    margin-bottom: 6px;
    white-space: nowrap;
  }
  .contact__item svg { width: 10px; height: 10px; flex: none; }
  .social {
    display: flex;
    align-items: center;
    gap: 4px;
    margin-top: 4px;
  }
  .social__mark {
    width: 13px;
    height: 13px;
    border-radius: 50%;
    background: var(--red);
    flex: none;
  }
  .social__mark--mid { background: var(--social-mid); }
  .social__mark--dark { background: var(--social-dark); }
  .social__handle {
    margin-left: 4px;
    font-size: 10.5px;
    font-weight: 600;
    color: var(--red);
  }
  .tagline-band {
    position: absolute;
    right: 0;
    bottom: 0;
    width: 250px;
    height: 58px;
    background: var(--red);
    border-top-left-radius: 16px;
    display: flex;
    align-items: flex-end;
    justify-content: center;
    padding-bottom: 14px;
  }
  .tagline-band__text {
    color: #fff;
    font-size: 12px;
    font-weight: 600;
  }
</style>
</head>
<body>
  <main class="sheet">
    <section class="card card--logo" aria-label="Logo side">
      <div class="brand">
        <span class="brand__dot"></span>
        <span class="brand__name">Brightwire Hollow</span>
      </div>
    </section>

    <section class="card card--details" aria-label="Details side">
      <div class="brand">
        <span class="brand__dot"></span>
        <span class="brand__name">Brightwire<br>Hollow</span>
      </div>

      <div class="contact">
        <p class="contact__name">Marcus Pell</p>
        <p class="contact__role">Managing Director</p>
        <ul class="contact__list">
          <li class="contact__item">
            <svg viewBox="0 0 10 10" aria-hidden="true"><path d="M2 1h2l1 2.3-1.2.8a5 5 0 0 0 2.1 2.1l.8-1.2L9 6v2a1 1 0 0 1-1 1A7 7 0 0 1 1 2a1 1 0 0 1 1-1z" fill="#e0261f"/></svg>
            0431 587 219
          </li>
          <li class="contact__item">
            <svg viewBox="0 0 10 10" aria-hidden="true"><rect x="0.5" y="2" width="9" height="6.5" rx="0.8" fill="#e0261f"/><path d="M0.8 2.4 5 5.6l4.2-3.2" stroke="#fff" stroke-width="0.9" fill="none"/></svg>
            marcus@brightwirehollow.com.au
          </li>
          <li class="contact__item">
            <svg viewBox="0 0 10 10" aria-hidden="true"><circle cx="5" cy="5" r="4.2" fill="none" stroke="#e0261f" stroke-width="1.1"/><path d="M0.8 5h8.4M5 0.8c-2 2.4-2 6 0 8.4M5 0.8c2 2.4 2 6 0 8.4" stroke="#e0261f" stroke-width="0.8" fill="none"/></svg>
            www.brightwirehollow.com.au
          </li>
        </ul>
        <div class="social">
          <span class="social__mark"></span>
          <span class="social__mark social__mark--mid"></span>
          <span class="social__mark social__mark--dark"></span>
          <span class="social__handle">brightwirehollow_au</span>
        </div>
      </div>

      <div class="tagline-band">
        <span class="tagline-band__text">24/7 Sydney Electrician</span>
      </div>
    </section>
  </main>
</body>
</html>
```